依頼詳細
★TOPラフ案について

・トップページの掲載内容はエクセルで作成した資料を添付しました。
仕様はワイヤーフレームのみですので、掲載情報が正しければ、お好きなデザインにて調整していただいて構いません。

掲載している情報のレイアウト通りではなくて大丈夫ですので
皆さまの感性にてお願いいたします。

・配置やデザイン等はアレンジしていただいて構いません。

・サイズは横幅2000pxで制作をお願いします。
縦に制限はありません。(コンテンツ幅は1100px~1200px内でお願いします。)
レスポンシブデザインのサイトで、bootstrap4を利用し、コーディングする予定になります。

・カラーイメージ
白を基調としてサブに青系、ワンポイントに赤色にてお願いします。

・ロゴ画像はヘッダーに入れる予定です。
(ロゴは青色(#00008B)で会社名ローマ字表示となります。頭文字は赤色(#FF3737)です。)

・デザインイメージ
誠実なデザインのイメージです。

デザイン選定後、決定した方には、正式な社名や連絡先を入れた修正をお願いしたいのと、
その他常識範囲で修正を依頼することもあります。
※以後、希望があれば中ページ作成及び他の案件コンテンツも継続してご依頼可能です。
ページ数
1ページ
希望イメージ
シンプル 複雑
単色 カラフル
暗い 明るい
日常 高級
遊び心 厳粛
未来的 伝統的
女性的 男性的
希望する色
青系
納品ファイル
• 高解像度JPG (.jpg)
• フォトショップ形式 (.psd)
補足説明
※ワイヤーフレーム通りのデザインでなくて、構いません。
メインビジュアル、素材などもお好みでデザインいただいて問題ございません。

仕様素材につきましてはZELNO定額素材内で使用可能な素材をご選択いただいてご使用ください。
(添付したデータ内にない素材でもご利用OKです。
その際は選定後素材№をお知らせください。)
■ 選んだ理由

依頼したイメージに沿ったデザインを作成いただけたためこちらのデザインに決めさせていただきました。

■ 提案者全員のお礼・コメント

多くの提案をいただき本当にありがとうございました。
次回の依頼の際も是非提案いただけますようお願いいたします。

```html
<!DOCTYPE html>
<html lang="ja">
<head>
<meta charset="UTF-8">
<title>梱包が変わると物流が変わる</title>
<link rel="stylesheet" href="https://fonts.googleapis.com/css2?family=Noto+Sans+JP:wght@400;500;700;900&family=Montserrat:wght@700;800&display=swap">
<style>
:root{
  --navy:#0d3a6b;
  --navy-dark:#0a2f58;
  --accent-blue:#3d9be0;
  --red:#ff3737;
  --text:#333;
  --muted:#777;
  --line:#cfd6de;
  --contact-bg:#eef2f6;
  --white:#fff;
}
*{margin:0;padding:0;box-sizing:border-box}
html,body{width:1200px;height:2548px;overflow:hidden;background:var(--white)}
body{font-family:"Noto Sans JP",sans-serif;color:var(--text);position:relative}
.abs{position:absolute}

/* header */
.site-header{position:absolute;left:0;top:0;width:1200px;height:120px}
.brand{left:148px;top:40px;font-weight:900;font-size:28px;color:var(--navy);letter-spacing:1px}
.global-nav{left:340px;top:50px;display:flex;gap:36px;font-size:16px;color:var(--text)}
.header-tel{left:862px;top:18px;font-size:22px;font-weight:700;color:var(--navy);display:flex;align-items:center;gap:10px}
.header-contact{left:850px;top:58px;width:206px;height:46px;background:var(--navy);color:var(--white);font-size:18px;font-weight:700;display:flex;align-items:center;justify-content:center;gap:10px}

/* hero */
.hero{left:132px;top:122px;width:936px;height:578px;background:linear-gradient(180deg,#4a5560 0%,#6a6a58 45%,#5c5b4a 75%,#3c4048 100%)}
.hero::after{content:"";position:absolute;inset:0;background:rgba(10,30,50,.35)}
.hero-copy{position:absolute;left:0;right:0;top:300px;text-align:center;color:var(--white);font-weight:900;font-size:66px;line-height:1.45;font-style:italic;letter-spacing:2px;z-index:1}

/* feature blocks */
.feature-panel{background:var(--navy);color:var(--white);text-align:center}
.feature-title{font-family:"Montserrat",sans-serif;font-weight:800;font-size:50px;letter-spacing:1px;line-height:1.2}
.feature-sub{color:var(--red);font-size:16px;margin-top:2px}
.feature-body{font-size:14px;line-height:1.75;margin-top:16px}
.btn-more{display:inline-block;margin-top:18px;background:var(--accent-blue);color:var(--white);font-size:15px;font-weight:700;padding:8px 38px}
.about-panel{left:132px;top:776px;width:400px;height:276px;padding-top:20px}
.about-photo{left:512px;top:760px;width:480px;height:280px;background:linear-gradient(160deg,#8fa8c2 0%,#c9c2ad 50%,#8c8f95 100%)}
.packing-photo{left:208px;top:1100px;width:480px;height:284px;background:linear-gradient(135deg,#c8d4de 0%,#b38f63 55%,#6a8fb8 100%)}
.packing-panel{left:680px;top:1110px;width:388px;height:300px;padding-top:20px}

/* news */
.section-title{font-weight:700;font-size:30px;color:var(--navy);text-align:center}
.section-title::after{content:"";display:block;width:60px;height:3px;background:var(--navy);margin:10px auto 0}
.news-title{left:0;top:1460px;width:1200px}
.news-list{left:232px;top:1545px;width:748px;list-style:none}
.news-item{display:flex;align-items:center;gap:20px;min-height:62px;padding:10px 0;border-bottom:1px solid var(--line);font-size:15px}
.news-date{flex:0 0 70px;color:var(--muted);font-size:13px;white-space:nowrap}
.news-tag{flex:0 0 auto;white-space:nowrap;background:var(--accent-blue);color:var(--white);font-size:12px;padding:3px 12px}
.news-text{flex:1 1 auto;min-width:0;word-break:break-all;line-height:1.5}
.news-more{left:520px;top:1830px;width:160px;height:36px;border-radius:18px;background:var(--accent-blue);color:var(--white);font-family:"Montserrat",sans-serif;font-size:13px;font-weight:700;display:flex;align-items:center;justify-content:center}

/* contact */
.contact{left:132px;top:1932px;width:936px;height:262px;background:var(--contact-bg)}
.contact .section-title{margin-top:14px;font-size:28px}
.contact-col{position:absolute;top:96px;width:380px;text-align:center}
.contact-col h3{font-size:16px;font-weight:700;color:var(--text)}
.contact-tel{margin-top:20px;font-size:26px;font-weight:700;color:var(--navy);display:flex;align-items:center;justify-content:center;gap:10px}
.contact-hours{font-size:12px;color:var(--muted);margin-top:6px}
.contact-mail{display:inline-flex;align-items:center;gap:10px;margin-top:18px;background:var(--navy);color:var(--white);font-size:18px;font-weight:700;padding:12px 24px}

/* footer */
.site-footer{left:132px;top:2208px;width:936px;height:340px;background:var(--navy-dark);color:var(--white)}
.footer-nav{position:absolute;top:30px;left:0;width:100%;display:flex;justify-content:center;gap:44px;font-size:15px}
.footer-company{position:absolute;left:26px;top:88px;font-size:14px;line-height:2.2}
.footer-company strong{font-size:22px;display:block;line-height:1.4;margin-bottom:6px}
.footer-map{position:absolute;left:368px;top:82px;width:320px;height:200px;background:linear-gradient(135deg,#e8e6df,#d3dbe2)}
.footer-link{position:absolute;left:720px;top:150px;width:188px;height:86px;border:1px solid var(--white);display:flex;align-items:center;justify-content:center;font-size:16px}
.copyright{position:absolute;left:0;bottom:14px;width:100%;text-align:center;font-size:12px}
</style>
</head>
<body>

<header class="site-header">
  <div class="abs brand">LOGO</div>
  <nav class="abs global-nav"><span>ホーム</span><span>○○○○について</span><span>業務案内</span><span>会社概要</span></nav>
  <div class="abs header-tel">
    <svg width="18" height="18" viewBox="0 0 24 24"><path fill="#0d3a6b" d="M6.6 10.8a15 15 0 0 0 6.6 6.6l2.2-2.2c.3-.3.7-.4 1-.2 1.1.4 2.3.6 3.6.6.6 0 1 .4 1 1V20c0 .6-.4 1-1 1A17 17 0 0 1 3 4c0-.6.4-1 1-1h3.5c.6 0 1 .4 1 1 0 1.3.2 2.5.6 3.6.1.3 0 .7-.2 1z"/></svg>
    00-0000-0000
  </div>
  <div class="abs header-contact">
    <svg width="20" height="16" viewBox="0 0 20 16"><rect x="1" y="1" width="18" height="14" fill="none" stroke="#fff" stroke-width="2"/><path d="M1 1l9 7 9-7" fill="none" stroke="#fff" stroke-width="2"/></svg>
    お問い合わせ
  </div>
</header>

<section class="abs hero" role="img" aria-label="倉庫内に積まれた段ボール箱の写真">
  <h1 class="hero-copy">梱包が変わると<br>物流が変わる</h1>
</section>

<section>
  <div class="abs about-photo" role="img" aria-label="倉庫内で作業するスタッフの写真"></div>
  <div class="abs feature-panel about-panel">
    <h2 class="feature-title">ABOUT</h2>
    <p class="feature-sub">○○○○について</p>
    <p class="feature-body">2021年に○○○○から社名を変更した<br>「株式会社○○○○」<br>梱包のトータルサポートを提供し<br>確かなサービスをお約束いたします。</p>
    <span class="btn-more">詳しくみる</span>
  </div>
</section>

<section>
  <div class="abs packing-photo" role="img" aria-label="段ボール箱にテープを貼る梱包作業の写真"></div>
  <div class="abs feature-panel packing-panel">
    <h2 class="feature-title">PACKING</h2>
    <p class="feature-sub">業務案内</p>
    <p class="feature-body">梱包の専門会社として、お客様のニーズに合った<br>最適・最善のサービスをお届けいたします。<br>モノづくりの全ての工程に携わりながら<br>「梱包の未来」を追求します。</p>
    <span class="btn-more">詳しくみる</span>
  </div>
</section>

<section>
  <h2 class="abs section-title news-title">お知らせ</h2>
  <ul class="abs news-list">
    <li class="news-item"><span class="news-date">2021/7/1</span><span class="news-tag">お知らせ</span><span class="news-text">xxx○○○○○○○○○○○○○○○○○○○○○○○○○○○○○○○○○○○○○○○</span></li>
    <li class="news-item"><span class="news-date">2021/7/1</span><span class="news-tag">お知らせ</span><span class="news-text">xxx○○○○○○○○○○○○○○○○○</span></li>
    <li class="news-item"><span class="news-date">2021/7/1</span><span class="news-tag">お知らせ</span><span class="news-text">xxx○○○○○○○○○○○○○○○○○</span></li>
    <li class="news-item"><span class="news-date">2021/7/1</span><span class="news-tag">お知らせ</span><span class="news-text">xxx○○○○○○○○○○○○○○○○○</span></li>
  </ul>
  <div class="abs news-more">VIEW MORE</div>
</section>

<section class="abs contact">
  <h2 class="section-title">お問合せ</h2>
  <div class="contact-col" style="left:50px">
    <h3>お電話でのお問い合わせ</h3>
    <div class="contact-tel">
      <svg width="22" height="22" viewBox="0 0 24 24"><path fill="#0d3a6b" d="M6.6 10.8a15 15 0 0 0 6.6 6.6l2.2-2.2c.3-.3.7-.4 1-.2 1.1.4 2.3.6 3.6.6.6 0 1 .4 1 1V20c0 .6-.4 1-1 1A17 17 0 0 1 3 4c0-.6.4-1 1-1h3.5c.6 0 1 .4 1 1 0 1.3.2 2.5.6 3.6.1.3 0 .7-.2 1z"/></svg>
      00-0000-0000
    </div>
    <p class="contact-hours">8:00〜17:00（平日）</p>
  </div>
  <div class="contact-col" style="left:500px">
    <h3>メールでのお問い合わせ</h3>
    <span class="contact-mail">
      <svg width="20" height="16" viewBox="0 0 20 16"><rect x="1" y="1" width="18" height="14" fill="none" stroke="#fff" stroke-width="2"/><path d="M1 1l9 7 9-7" fill="none" stroke="#fff" stroke-width="2"/></svg>
      メールフォームはこちら
    </span>
  </div>
</section>

<footer class="abs site-footer">
  <nav class="footer-nav"><span>ホーム</span><span>○○○○について</span><span>業務案内</span><span>会社概要</span></nav>
  <div class="footer-company">
    <strong>株式会社○○○○</strong>
    〒123-1111 東京都○○区○○町1丁目1-1<br>
    TEL：00-0000-0000<br>
    FAX：00-0000-0000
  </div>
  <div class="footer-map" role="img" aria-label="所在地の地図"></div>
  <div class="footer-link">リンク</div>
  <p class="copyright">©2021株式会社○○○○</p>
</footer>

</body>
</html>
```